letterhead design

can you create a letterhead using the logo you created and the following:

318 W Dunthorpe Elgin IL 60187
(p) 847-512-3971
(f) 847-438-1065
www.thekestrinlawgroup.example

Industry/Entity Type

Law

Requirements
Must have
• Use logo attached: must have address 318 W Dunthorpe Elgin IL 60187 phone 847-512-3971 fax 847-438-1065
Should not have
• Nothing other thank logo and address/phone/website

```html
<!DOCTYPE html>
<html lang="en">
<head>
<meta charset="utf-8">
<title>Kestrin Law Group — Letterhead</title>
<link rel="stylesheet" href="https://fonts.googleapis.com/css2?family=Libre+Baskerville&display=swap">
<style>
  :root {
    --backdrop: #3d3d3d;
    --paper: #f4f4f4;
    --ink: #050608;
    --gold: #e3b35b;
    --text: #1c1c1c;
    --icon: #6a6258;
  }
  * { margin: 0; padding: 0; box-sizing: border-box; }
  html, body { width: 1200px; height: 1200px; overflow: hidden; background: var(--backdrop); }
  .letterhead {
    position: absolute; left: 243px; top: 94px; width: 714px; height: 1011px;
    background: var(--paper); overflow: hidden;
    font-family: "Libre Baskerville", Georgia, serif; color: var(--text);
  }
  .letterhead__photo {
    position: absolute; inset: 0;
    background:
      radial-gradient(ellipse 30% 55% at 78% 55%, rgba(190,190,190,.55), rgba(190,190,190,0) 70%),
      radial-gradient(ellipse 40% 30% at 20% 70%, rgba(205,205,205,.5), rgba(205,205,205,0) 70%),
      linear-gradient(180deg, #f1f1f1 0%, #e6e6e6 45%, #ececec 80%, #f2f2f2 100%);
  }
  .letterhead__bands { position: absolute; inset: 0; width: 714px; height: 1011px; }
  .brand {
    position: absolute; left: 47px; top: 50px; width: 166px; text-align: center;
  }
  .brand__mark {
    display: block; width: 64px; height: 64px; margin: 0 auto 14px;
    border: 1.6px solid var(--ink); border-radius: 50%;
  }
  .brand__name { font-size: 19px; letter-spacing: .5px; line-height: 1; color: var(--ink); }
  .brand__sub { font-size: 10px; letter-spacing: 1.5px; margin-top: 6px; color: var(--ink); }
  .contact {
    position: absolute; left: 425px; top: 864px; font-size: 13.5px; line-height: 1;
  }
  .contact__row { display: flex; align-items: center; height: 20px; margin-bottom: 12px; }
  .contact__item { display: flex; align-items: center; margin-right: 18px; }
  .contact__icon { width: 20px; height: 20px; margin-right: 11px; fill: var(--icon); }
</style>
</head>
<body>
<main class="letterhead">
  <div class="letterhead__photo" role="img" aria-label="Faded black-and-white photo of a Lady Justice statue holding scales"></div>

  <svg class="letterhead__bands" viewBox="0 0 714 1011" aria-hidden="true">
    <polygon points="27,0 714,0 714,72" fill="var(--ink)"/>
    <polygon points="204,22 714,72 714,110" fill="var(--gold)"/>
    <line x1="427" y1="64" x2="714" y2="120" stroke="var(--gold)" stroke-width="0.8"/>
    <polygon points="0,898 509,990 0,936" fill="var(--gold)"/>
    <polygon points="0,936 701,1011 0,1011" fill="var(--ink)"/>
    <line x1="0" y1="890" x2="484" y2="980" stroke="var(--gold)" stroke-width="0.8"/>
  </svg>

  <div class="brand">
    <span class="brand__mark"></span>
    <div class="brand__name">KESTRIN LAW</div>
    <div class="brand__sub">GROUP</div>
  </div>

  <div class="contact">
    <div class="contact__row">
      <span class="contact__item">
        <svg class="contact__icon" viewBox="0 0 20 20" aria-label="Phone"><path d="M2 7c0-2 4-4 8-4s8 2 8 4v2h-4V7H6v2H2z"/><rect x="4" y="10" width="12" height="8" rx="1"/></svg>
        847-512-3971
      </span>
      <span class="contact__item">
        <svg class="contact__icon" viewBox="0 0 20 20" aria-label="Fax"><rect x="2" y="8" width="4" height="10"/><rect x="7" y="2" width="9" height="7"/><rect x="7" y="10" width="11" height="8"/></svg>
        847-438-1065
      </span>
    </div>
    <div class="contact__row">
      <span class="contact__item">
        <svg class="contact__icon" viewBox="0 0 20 20" aria-label="Website"><circle cx="10" cy="10" r="8" fill="none" stroke="var(--icon)" stroke-width="2"/><path d="M2 10h16M10 2c-3 3-3 13 0 16M10 2c3 3 3 13 0 16" fill="none" stroke="var(--icon)" stroke-width="1.4"/></svg>
        www.thekestrinlawgroup.example
      </span>
    </div>
    <div class="contact__row">
      <span class="contact__item">
        <svg class="contact__icon" viewBox="0 0 20 20" aria-label="Address"><path d="M10 1a6 6 0 0 0-6 6c0 5 6 11 6 11s6-6 6-11a6 6 0 0 0-6-6zm0 8.5A2.5 2.5 0 1 1 10 4.5a2.5 2.5 0 0 1 0 5z"/></svg>
        318 W Dunthorpe Elgin IL 60187
      </span>
    </div>
  </div>
</main>
</body>
</html>
```